Corporate Business Card Design Project

..Hi designers!
I have established a consultancy within strategic communnications, for which I need a business card design - I've seen some of the things you do in here, and they're great! I'll provide some information in the following:
Name: BriarLedger
Tagline: Guiding Dialogue
Service: Strategic communications consulting (primariy internal communication and optimizing): various organisations - e.g. SMEs, NGOs and NPOs - are offered an analysis of their current efforts and, on the basis of that, management consulting tailored their unique challenges and needs.
It's a sole proprietorship - for now! - but it's my plan to employ 5-20 persons over the years. Therefore the card should NOT symbolize a start-up, but communicate a well-established, serious consultancy. Hence, it should also apply to serious companies and organizations - think Veltra or Hollis Brant Group (both as sender and receiver) ;)
The design should accordingly have a formal, conservative, stylish, corporate, clean look! and ditto colors, eg. black, grey, white etc - corresponding to the logo. The only colour that can appear is the same orange contrast as in my logo (see attachement). Not too bold or dramatic fonds or letters.
I choose the double sided as I think it gives the most professional look: One side with name, titel, phone, e-mail - then a little space - and four additional lines for address.
This composition is if all information should be in the same "column" - feel free to provide suggestions with the address places elsewhere on the one side.
On the other side, I'm only thinkin' something with the logo.
I'd be happy to see different ideas re. the use of the orange contrast, placement of logo, etc.
I do not plan on changing the design of businees cards ever - as I think it is more serious keeping a concept and avoid rebranding - and I'm sure that you can deliver an ever-lasting logo for my company! Thanks :).
Let's play the rest by ear in the correspondance.
Target Market(s)
Executive level: CEOs, HR directors, communication managers/directors, business owners.
Industry/Entity Type
Management Consulting

```html
<!DOCTYPE html>
<html lang="en">
<head>
<meta charset="utf-8">
<title>BriarLedger – Business Card</title>
<link rel="stylesheet" href="https://fonts.googleapis.com/css2?family=Tinos:wght@400&display=swap">
<style>
  :root {
    --backdrop: #4b4b4b;
    --card: #1f1f1f;
    --emboss: #3a3a3a;
    --logo-light: #d6d6d6;
    --text-light: #e2e2e2;
    --accent: #f28a22;
  }
  * { margin: 0; padding: 0; box-sizing: border-box; }
  html, body { width: 1200px; height: 1000px; overflow: hidden; }
  body {
    background: var(--backdrop);
    font-family: "Tinos", "Times New Roman", serif;
    position: relative;
  }
  .card {
    position: absolute;
    background: var(--card);
    border-radius: 12px;
    overflow: hidden;
    box-shadow: 0 3px 6px rgba(0,0,0,0.35);
  }
  .card--front { left: 175px; top: 138px; width: 574px; height: 357px; }
  .card--back  { left: 445px; top: 540px; width: 582px; height: 360px; }

  .wordmark { position: absolute; white-space: nowrap; line-height: 1; }
  .wordmark__name { display: block; }
  .wordmark__tagline { display: block; letter-spacing: 0.16em; }

  .card--front .wordmark { left: 83px; top: 140px; color: var(--emboss); }
  .card--front .wordmark__name { font-size: 60px; }
  .card--front .wordmark__tagline { font-size: 14px; margin: 4px 0 0 172px; }

  .card--back .wordmark { left: 36px; top: 155px; color: var(--logo-light); }
  .card--back .wordmark__name { font-size: 37px; }
  .card--back .wordmark__tagline { font-size: 10px; margin: 2px 0 0 107px; color: #9a9a9a; }

  .details { position: absolute; left: 353px; top: 46px; color: var(--text-light); }
  .details__name { color: var(--accent); font-size: 21px; line-height: 24px; }
  .details__title { font-size: 15px; line-height: 20px; }
  .contact { list-style: none; margin-top: 44px; font-size: 13px; }
  .contact li { display: flex; align-items: center; gap: 6px; height: 21.5px; }
  .contact svg { width: 14px; height: 14px; fill: var(--accent); }
  .address { margin-top: 45px; font-size: 13px; line-height: 22px; }
  .address__company { color: var(--accent); font-size: 17px; line-height: 22px; margin-bottom: 1px; }

  .accent-band {
    position: absolute; left: 0; right: 0; bottom: 2px; height: 19px;
    background: var(--accent);
  }
</style>
</head>
<body>

<section class="card card--front" aria-label="Business card front">
  <div class="wordmark">
    <span class="wordmark__name">BriarLedger</span>
    <span class="wordmark__tagline">Guiding Dialogue</span>
  </div>
</section>

<section class="card card--back" aria-label="Business card back">
  <div class="wordmark">
    <span class="wordmark__name">BriarLedger</span>
    <span class="wordmark__tagline">Guiding Dialogue</span>
  </div>

  <div class="details">
    <p class="details__name">Julian Ashby</p>
    <p class="details__title">Chief Executive Officer</p>

    <ul class="contact">
      <li>
        <svg viewBox="0 0 16 16" aria-hidden="true"><path d="M3.5 1.5l2.5 3-1.5 1.8c.9 1.9 2.3 3.3 4.2 4.2l1.8-1.5 3 2.5-1.6 2.6C6.6 13.8 2.2 9.4 1 3.1z"/></svg>
        +45 31 64 08 57
      </li>
      <li>
        <svg viewBox="0 0 16 16" aria-hidden="true"><path d="M1 3h14v10H1zM2 4l6 5 6-5z" fill-rule="evenodd"/></svg>
        ashby@briarledger.dk
      </li>
      <li>
        <svg viewBox="0 0 16 16" aria-hidden="true"><circle cx="8" cy="8" r="6.5"/><path d="M5 4.5c1.5.5 2 2 1 3s-.5 2.5 1 3M10 3.5c-.5 1.5.5 2.5 2 2.5M9.5 12c.5-1 1.5-1.5 2.5-1" stroke="#1f1f1f" stroke-width="1.2" fill="none"/></svg>
        www.briarledger.dk
      </li>
    </ul>

    <div class="address">
      <p class="address__company">BriarLedger</p>
      <p>Kestrelvej 18</p>
      <p>First Floor, Door 2</p>
      <p>DK-4100 Havnsted</p>
    </div>
  </div>

  <div class="accent-band"></div>
</section>

</body>
</html>
```